Business Card Re-Design

Consulting Company: To build a high performance organization, you need great leaders at all levels throughout your organization. The Northvale Talent Growth Studio engages, inspires, and educates current and future leaders to step beyond the ordinary and deliver exceptional results. This new breed of leaders will motivate your staff to leave the safety of complacency behind and come together to build an extraordinary organization. The current trend has been to ask our people to do more with fewer resources. People have been stepping up to the challenge, but more is required to ensure success with a new work paradigm. We work with your management team to build a successful strategy that will make your organization more effective. NTGS then supports your management team by providing a comprehensive set of proven services to empower your entire organization to successfully execute new strategies.Let NTGS help you optimize your organization’s individual and team performance today!

Target Market(s)

Federal, State and Local Government / Non profit

Industry/Entity Type

Management Consulting

Contact Information for Business Card

NTGS, inc (Northvale Talent Growth Studio) Optimizing Individual and Organizational Performance

Colors
fee18a
ec1f27
474747
fbf289

Requirements
Must have
• Professional and high quality feel

```html
<!DOCTYPE html>
<html lang="en">
<head>
<meta charset="utf-8">
<title>NTGS, inc — Business Card</title>
<link rel="stylesheet" href="https://fonts.googleapis.com/css2?family=Open+Sans:wght@400;600;700&display=swap">
<style>
  :root {
    --backdrop: #d6d6d6;
    --card-grey: #8e8e8e;
    --card-black: #070707;
    --swoosh: #bfbfbf;
    --accent-yellow: #fee18a;
    --accent-red: #ec1f27;
    --logo-light: #c4c4c4;
    --logo-faint: #7b7b7b;
    --text-white: #ffffff;
  }
  * { margin: 0; padding: 0; box-sizing: border-box; }
  html, body {
    width: 1200px; height: 900px; overflow: hidden;
    background: var(--backdrop);
    font-family: "Open Sans", Arial, sans-serif;
  }
  .canvas {
    width: 1200px; height: 900px;
    display: flex; flex-direction: column;
    align-items: center; justify-content: center; gap: 44px;
  }
  .card {
    position: relative;
    width: 560px; height: 320px;
    background: var(--card-grey);
    overflow: hidden;
    box-shadow: 0 6px 18px rgba(0,0,0,0.18);
  }
  .card-back {
    display: flex; flex-direction: column; align-items: center; justify-content: center;
    border-bottom: 3px solid var(--accent-yellow);
  }

  /* brand block: one colour, one weight */
  .brand { font-weight: 700; line-height: 1; }
  .brand-small { font-size: 15px; letter-spacing: 1px; text-transform: uppercase; }
  .brand-big { font-size: 80px; letter-spacing: -2px; margin: 4px 0 6px; }

  .card-back .brand { color: var(--logo-faint); text-align: center; }
  .tagline {
    margin-top: 18px; font-size: 12px; font-weight: 600;
    letter-spacing: 1.5px; text-transform: uppercase; color: var(--logo-faint);
  }

  .front-shape { position: absolute; inset: 0; }
  .card-front .brand {
    position: absolute; left: 36px; top: 86px;
    color: var(--logo-light);
  }

  .contact {
    position: absolute; right: 36px; top: 62px;
    text-align: right; color: var(--text-white);
  }
  .contact-name { font-size: 18px; font-weight: 700; letter-spacing: 0.3px; line-height: 1.1; }
  .contact-title { font-size: 13px; font-weight: 600; margin-bottom: 10px; }
  .contact-address { font-size: 14px; line-height: 1.3; margin-bottom: 14px; }
  .contact-line {
    display: flex; justify-content: flex-end; align-items: center; gap: 10px;
    font-size: 14px; line-height: 1.45;
  }
  .contact-line svg { width: 11px; height: 11px; fill: var(--text-white); flex: none; }
</style>
</head>
<body>
<main class="canvas">

  <section class="card card-back" aria-label="Card back">
    <div class="brand">
      <p class="brand-small">Northvale Talent</p>
      <p class="brand-big">NTGS</p>
      <p class="brand-small">Growth Studio, inc</p>
    </div>
    <p class="tagline">Optimizing Individual and Organizational Performance</p>
  </section>

  <section class="card card-front" aria-label="Card front">
    <svg class="front-shape" viewBox="0 0 560 320" width="560" height="320" aria-hidden="true">
      <path d="M236 0 H268 C352 78 326 250 196 320 H168 C290 248 318 84 236 0 Z" fill="var(--swoosh)"/>
      <path d="M0 0 H244 C326 78 300 248 176 320 H0 Z" fill="var(--card-black)"/>
      <path d="M252 0 C332 80 312 250 186 320" fill="none" stroke="var(--accent-red)" stroke-width="2"/>
    </svg>

    <div class="brand">
      <p class="brand-small">Northvale Talent</p>
      <p class="brand-big">NTGS</p>
      <p class="brand-small">Growth Studio, inc</p>
    </div>

    <div class="contact">
      <p class="contact-name">MARCUS L. HALE</p>
      <p class="contact-title">President/CEO</p>
      <p class="contact-address">4200 Linden Crest Way<br>Fairhaven, MD 20614</p>
      <p class="contact-line">301.555.0142
        <svg viewBox="0 0 24 24"><path d="M6.6 10.8a15.1 15.1 0 0 0 6.6 6.6l2.2-2.2a1 1 0 0 1 1-.25 11.4 11.4 0 0 0 3.6.57 1 1 0 0 1 1 1V20a1 1 0 0 1-1 1A17 17 0 0 1 3 4a1 1 0 0 1 1-1h3.5a1 1 0 0 1 1 1c0 1.25.2 2.45.57 3.57a1 1 0 0 1-.25 1z"/></svg>
      </p>
      <p class="contact-line">301.555.0187
        <svg viewBox="0 0 24 24"><path d="M6 2h10v5H6zM4 8h16a2 2 0 0 1 2 2v10H2V10a2 2 0 0 1 2-2zm3 4v2h2v-2zm4 0v2h2v-2zm4 0v2h2v-2zm-8 4v2h2v-2zm4 0v2h2v-2zm4 0v2h2v-2z"/></svg>
      </p>
      <p class="contact-line">mhale@ntgsmail.com
        <svg viewBox="0 0 24 24"><path d="M2 5h20v14H2zm2 2v.5l8 5 8-5V7zm0 2.8V17h16V9.8l-8 5z"/></svg>
      </p>
    </div>
  </section>

</main>
</body>
</html>
```